Financial planning wealth advisor Business Card

We have a finanancial advisory that caters to high net worth and business owner clients. We would like a card that works with our entire style. Please visit out website brightharborplanning.com to get a look and feel.... VERY OPEN to interesting and unique designs that have cutouts, fold overs, anything to capture interest...

Requirements, info must be the following:

Harbor Light Planning (with Logo)
Investments | Insurance | Retirement | Education | Estate | Business Planning

Nora Valk Penhallow, CFP, MSFS, AEP
Principal

915-720-5814 (Main)
915-286-9051 (Cell)
epenhallow@brightharborplanning.com

Central Location:
518 W Marlowe Suite 740
El Paso TX 79935

West Location:
2613 Thistlegate Lane SuiteB
El Paso TX 79948

brightharborplanning.com

DISCLOSURES (Back of Card)
Eleanor Valk Penhallow, CFP, MSFS, AEP, a Registered Representative offering securities through QUILLMARK Brokerage LLC. 518 W Marlowe Suite 740 El Paso TX 79935 915-867-2409. Member BRAVEN/TOLLIC, a licensed insurance agency.

*Financial Adviser offering investment advisory services through Juniper Advisory, LLC, a Registered Investment Advisor.

Harbor Light Planning is not owned or operated by QUILLMARK Brokerage LLC or its affiliates.

Target Market(s)

High end affluent or ultra rich clientele

Industry/Entity Type

Financial Planning

Font styles to use
Decorative

Requirements
Must have
• Needs to have something that focuses our services. :33 bellow for our original business card.

```html
<!DOCTYPE html>
<html lang="en">
<head>
<meta charset="utf-8">
<title>Harbor Light Planning – Business Card</title>
<link rel="stylesheet" href="https://fonts.googleapis.com/css2?family=Open+Sans:wght@400;600;700&display=swap">
<style>
  :root {
    --stage: #5a5a5a;
    --gold: #c9a868;
    --navy: #1d2a6b;
    --white: #ffffff;
    --ink: #1d2a6b;
  }
  * { margin: 0; padding: 0; box-sizing: border-box; }
  html, body { width: 1200px; height: 950px; overflow: hidden; }
  body {
    background: var(--stage);
    font-family: "Open Sans", Arial, sans-serif;
    position: relative;
  }
  .card {
    position: absolute;
    width: 700px;
    height: 400px;
    border-radius: 4px;
    overflow: hidden;
    box-shadow: 0 10px 30px rgba(0,0,0,.35);
  }
  /* Back card */
  .card-back {
    left: 80px; top: 55px;
    background: var(--gold);
    color: var(--white);
    text-align: center;
  }
  .card-back .brand {
    position: absolute; top: 110px; left: 0; right: 0;
    display: flex; align-items: center; justify-content: center; gap: 14px;
    font-size: 34px; font-weight: 600; letter-spacing: 1px;
  }
  .brand .brand-dot {
    width: 22px; height: 22px; border-radius: 50%;
    background: currentColor;
  }
  .card-back .services {
    position: absolute; top: 232px; left: 0; right: 0;
    font-size: 15px; font-weight: 700;
  }
  .card-back .disclosure {
    position: absolute; top: 270px; left: 40px; right: 40px;
    font-size: 11px; line-height: 1.55;
  }
  /* Front card */
  .card-front {
    left: 420px; top: 495px;
    background: var(--white);
  }
  .card-front svg { position: absolute; inset: 0; }
  .card-front .brand {
    position: absolute; left: 40px; top: 170px;
    display: flex; align-items: center; gap: 10px;
    color: var(--navy);
    font-size: 22px; font-weight: 600;
  }
  .card-front .brand .brand-dot { width: 16px; height: 16px; }
  .person { position: absolute; left: 40px; top: 222px; color: var(--navy); }
  .person .name { font-size: 24px; font-weight: 700; }
  .person .creds { font-size: 16px; font-weight: 700; margin-top: 2px; }
  .person .role { font-size: 16px; color: var(--gold); margin-top: 8px; }
  .contact {
    position: absolute; right: 30px; top: 92px;
    text-align: right; color: var(--white);
    font-size: 15px; line-height: 1.5;
  }
  .contact strong { font-weight: 700; }
  .contact .web { font-size: 14px; }
  .contact .heading { font-weight: 700; margin-top: 10px; }
</style>
</head>
<body>

<section class="card card-back">
  <div class="brand"><span class="brand-dot"></span>Harbor Light Planning</div>
  <p class="services">Investments | Insurance | Retirement | Education | Estate | Business Planning</p>
  <p class="disclosure">Eleanor Valk Penhallow, CFP, MSFS, AEP, a Registered Representative offering securities through QUILLMARK Brokerage LLC. 518 W Marlowe Suite 740 El Paso TX 79935 915-867-2409. Member BRAVEN/TOLLIC, a licensed insurance agency. *Financial Adviser offering investment advisory services through Juniper Advisory, LLC, a Registered Investment Advisor. Harbor Light Planning is not owned or operated by QUILLMARK Brokerage LLC or its affiliates.</p>
</section>

<section class="card card-front">
  <svg width="700" height="400" viewBox="0 0 700 400" aria-hidden="true">
    <path class="navy-field" d="M480,0 Q340,230 262,400 L700,400 L700,0 Z" fill="var(--navy)"/>
    <path class="gold-swoosh" d="M225,400 Q340,180 452,48 L440,40 L478,18 L470,60 L460,54 Q358,190 252,400 Z" fill="var(--gold)"/>
  </svg>

  <div class="brand"><span class="brand-dot"></span>Harbor Light Planning</div>

  <div class="person">
    <p class="name">Nora Valk Penhallow</p>
    <p class="creds">CFP , MSFS, AEP</p>
    <p class="role">Principal</p>
  </div>

  <div class="contact">
    <p><strong>Phone:</strong> 915-720-5814</p>
    <p><strong>Mob:</strong> 915-286-9051</p>
    <p class="web">epenhallow@brightharborplanning.com</p>
    <p class="web">brightharborplanning.com</p>
    <p class="heading">Central Location</p>
    <p>518 W Marlowe Suite 740, El Paso TX 79935</p>
    <p class="heading">West Location</p>
    <p>2613 Thistlegate Lane SuiteB, El Paso TX 79948</p>
  </div>
</section>

</body>
</html>
```